Larkspur Ridge Management - Business Cards

I need business cards. My current logo was designed by a designer at this site and I very much like and am happy with the results. I would like a business card that is trendy, unique, current yet professional. I deal with high net worth clients daily

Target Market(s)

Out of state investors looking to get into the rental market in Ohio

Industry/Entity Type

Property Management, Consulting

Contact Information for Business Card

Name, Title (Chief Financial Officer) office phone number (555) 817-3094 website address larkridgemgmt.example

Font styles to use
Sans Serif

Colors
0054AA
0677BA
7BADD7
CADEEF
E8F1F8
0094D4
00A9DD
6FCCEA
C7EBF8
E9F6FB
00AB8E
00BBA5
67D7C9
C6EFE9
E9F9F6

```html
<!DOCTYPE html>
<html lang="en">
<head>
<meta charset="utf-8">
<title>Larkspur Ridge Management – Business Cards</title>
<link href="https://fonts.googleapis.com/css2?family=Montserrat:wght@400;500;700&display=swap" rel="stylesheet">
<style>
  :root {
    --stage: #5f5f5e;
    --navy: #23335a;
    --navy-deep: #1c2a4d;
    --red: #c3282e;
    --paper: #ffffff;
    --ink: #1f2b4a;
    --muted: #2a3553;
  }
  * { margin: 0; padding: 0; box-sizing: border-box; }
  html, body {
    width: 1200px; height: 1200px; overflow: hidden;
    background: var(--stage);
    font-family: "Montserrat", Arial, sans-serif;
  }
  .card {
    position: absolute; left: 200px; width: 800px; height: 490px; overflow: hidden;
  }
  .card-front {
    top: 80px;
    background: radial-gradient(ellipse at center, #2a3c66 0%, var(--navy) 55%, var(--navy-deep) 100%);
    display: flex; align-items: center; justify-content: center;
  }
  .front-wordmark {
    display: flex; align-items: center; gap: 18px;
    color: var(--paper); font-weight: 700; font-size: 40px; letter-spacing: 0.5px;
  }
  .wordmark-square { width: 26px; height: 26px; background: var(--red); flex: none; }

  .card-back { top: 632px; background: var(--paper); }
  .back-bands { position: absolute; inset: 0; }
  .person-name {
    position: absolute; left: 67px; top: 112px;
    font-size: 50px; font-weight: 700; color: var(--ink); letter-spacing: -0.5px;
  }
  .person-title {
    position: absolute; left: 67px; top: 176px;
    font-size: 29px; font-weight: 400; color: var(--muted);
  }
  .divider {
    position: absolute; left: 67px; top: 222px; width: 680px; height: 3px; background: var(--red);
  }
  .contact {
    position: absolute; left: 67px; font-size: 31px; font-weight: 500; color: var(--ink);
  }
  .contact b { font-weight: 700; }
  .contact-phone { top: 268px; }
  .contact-web { top: 320px; }
  .back-wordmark {
    position: absolute; right: 52px; top: 382px; width: 200px; text-align: center;
    font-size: 17px; font-weight: 700; color: var(--navy); line-height: 1.25;
  }
</style>
</head>
<body>
  <section class="card card-front" aria-label="Card front">
    <div class="front-wordmark">
      <span class="wordmark-square"></span>
      <span>Larkspur Ridge Management</span>
    </div>
  </section>

  <section class="card card-back" aria-label="Card back">
    <svg class="back-bands" width="800" height="490" viewBox="0 0 800 490">
      <polygon points="413,0 800,0 800,22 429,22" fill="#23335a"/>
      <polygon points="0,468 533,468 519,490 0,490" fill="#23335a"/>
      <polygon points="555,468 800,468 800,490 541,490" fill="#c3282e"/>
    </svg>
    <div class="person-name">[Name]</div>
    <div class="person-title">Chief Financial Officer</div>
    <div class="divider"></div>
    <div class="contact contact-phone"><b>O:</b> (555) 817-3094</div>
    <div class="contact contact-web"><b>W:</b> larkridgemgmt.example</div>
    <div class="back-wordmark">Larkspur Ridge Management</div>
  </section>
</body>
</html>
```